Visitenkarte und Briefdesign
Zielgruppe
Limousinenservice (Stretchlimousinen)
Aufgabenstellung
Ich benötige eine Visitenkarte und ein Briefdesign in einer edlen Optik.
Auf folgender Seite können Informationen oder Bilder eingeholt werden
www.stretch-fahrten-nord.de
Ich mag einen Hintergrund in einer Lederoptik,( wie das Logo in Anhang, BILD x4)

```html
<!DOCTYPE html>
<html lang="de">
<head>
<meta charset="utf-8">
<title>Visitenkarte NV PRESTIGE</title>
<link href="https://fonts.googleapis.com/css2?family=Arimo:wght@700&family=Tinos:ital@0;1&display=swap" rel="stylesheet">
<style>
  :root {
    --page: #c9c9c9;
    --leather-light: #6a6a6a;
    --leather-mid: #3f3f3f;
    --leather-dark: #1e1e1e;
    --band: #ffffff;
    --ink: #111111;
    --text-light: #ffffff;
    --mark: #d8d8d8;
  }
  html, body {
    margin: 0;
    padding: 0;
    width: 891px;
    height: 1200px;
    overflow: hidden;
    background: var(--page);
  }
  .sheet {
    position: relative;
    width: 891px;
    height: 1200px;
  }
  .card {
    position: absolute;
    left: 60px;
    width: 771px;
    height: 502px;
    overflow: hidden;
  }
  .card--front { top: 60px; }
  .card--back { top: 633px; }
  .leather {
    position: absolute;
    inset: 0;
    background: radial-gradient(ellipse at 55% 40%, var(--leather-light) 0%, var(--leather-mid) 45%, var(--leather-dark) 100%);
  }
  .band {
    position: absolute;
    right: 0;
    height: 35px;
    background: var(--band);
    font-family: "Arimo", Arial, sans-serif;
    font-weight: 700;
    font-size: 29px;
    line-height: 35px;
    color: var(--ink);
    text-align: center;
    white-space: nowrap;
  }
  .card--front .band { top: 385px; left: 0; }
  .card--back .band { top: 80px; left: 33px; }
  .brand-mark {
    position: absolute;
    display: flex;
    flex-direction: column;
    align-items: center;
    gap: 14px;
    font-family: "Arimo", Arial, sans-serif;
    font-weight: 700;
    color: var(--mark);
    letter-spacing: 2px;
    white-space: nowrap;
  }
  .brand-mark__dot {
    width: 70px;
    height: 70px;
    border-radius: 50%;
    background: var(--mark);
  }
  .card--front .brand-mark {
    left: 0;
    width: 771px;
    top: 130px;
    font-size: 54px;
  }
  .card--back .brand-mark {
    left: 446px;
    width: 280px;
    top: 185px;
    font-size: 36px;
  }
  .card--back .brand-mark__dot { width: 50px; height: 50px; }
  .contact {
    position: absolute;
    left: 0;
    top: 0;
    width: 100%;
    height: 100%;
    font-family: "Tinos", "Times New Roman", serif;
    font-size: 21px;
    color: var(--text-light);
  }
  .contact__line {
    position: absolute;
    left: 74px;
    margin: 0;
    line-height: 24px;
    white-space: nowrap;
  }
  .contact__line--owner { top: 198px; }
  .contact__line--phone { top: 267px; }
  .contact__line--note { top: 300px; left: 82px; font-style: italic; font-size: 20px; }
  .contact__line--mail { top: 360px; }
  .contact__line--web { top: 396px; }
</style>
</head>
<body>
<main class="sheet">
  <section class="card card--front">
    <div class="leather" role="img" aria-label="Dunkelgraue Lederstruktur als Hintergrund"></div>
    <div class="brand-mark"><span class="brand-mark__dot"></span><span>NV PRESTIGE</span></div>
    <div class="band">Limousinenservice NV PRESTIGE</div>
  </section>

  <section class="card card--back">
    <div class="leather" role="img" aria-label="Dunkelgraue Lederstruktur als Hintergrund"></div>
    <div class="band">Limousinenservice NV PRESTIGE</div>
    <div class="contact">
      <p class="contact__line contact__line--owner">Inhaber: Markus Lindner</p>
      <p class="contact__line contact__line--phone">Tel.: 0170-5550187</p>
      <p class="contact__line contact__line--note">24 Stunden erreichbar</p>
      <p class="contact__line contact__line--mail">E-Mail: info@nv-prestige.de</p>
      <p class="contact__line contact__line--web">Internet: www.stretch-fahrten-nord.de / www.nv-prestige.de</p>
    </div>
    <div class="brand-mark"><span class="brand-mark__dot"></span><span>NV PRESTIGE</span></div>
  </section>
</main>
</body>
</html>
```